Health care equipment supplier needs a new website design

Our old website is tired but visiting it will give you a wealth of information about our products and services.

The why of my business:
Simply, I wanted to take the CRAP out of CPAP
Being told I needed to spend well over $2,000 for treatment was bullshit. The available options were limited, and all too expensive.
I wanted to know more, but was told very little.
I needed help, but didn't know who to trust.
I felt there must be a better way - but there wasn't.

We help thousands of people each year get a great night's sleep. Our customers wake up every morning feeling refreshed and energised, ready to take on the world.

The what of our business; Based on experience, we have a proven system for product selection and customer care that makes sleep apnea healthcare much more affordable.

Eventually, our new website will feature a combination of platforms such as wordpress (for us to easy edit sections) and an e-commerce cart like Magento to process online shop orders.

The brief
-----------
Provide a modern, home page design that considers the following requirements;

Emotional landing page that explains the 'why' of our business and builds trust.

Colours: Ideally Blue, grey, white being the colours of our logo

High contrast, large size font to cater for our more elderly demographic.
Search bar (at top of page)
The why of our business (text and video introduction)
Tops Sellers
Premium Range
Testimonials
Stay up to date - join our mailing list and receive $50 discount
Contact phone and email address clearly visible

Menu options
* About Us
* Contact Us
* Franchise
* New Arrivals
* Finance
* SHOP

The Home Page design theme will need to be adapted over the following pages in the future;
2. About Us
3. News Header (index of news article)
4. News Detail (show news article clicked from 3 above)
5. Shop Home Page
6. Shop Catalog Page - BOXES
7. Shop Catalog Page - LINES
8. Shop Product Page
9. Shopping Cart Page
10. Checkout Page
11. Customer Profile Page (self service account management)
12. FAQ Page

Target Market(s)

Age: 35~75
70% male

Industry/Entity Type

Health Care

Number of Pages Required

1 page

Font styles to use
Sans Serif

Requirements
Must have
• Emotional landing page that explains the 'why' of our business and builds trust.
• High contrast, large size font to cater for our more elderly demographic.
• Search bar (at top of page)
• The why of our business (text and video introduction)
• Tops Sellers
• Premium Range
• Testimonials
• Stay up to date - join our mailing list and receive $50 discount
• Contact phone and email address clearly visible
• Main Menu items\Menu options
• * About Us
• * Contact Us
• * Franchise
• * New Arrivals
• * Finance
• * SHOP
Nice to have
• Ideally Blue, grey, white being the colours of our logo
Should not have
• small font
• hard to read font
• Black backgound

```html
<!DOCTYPE html>
<html lang="en">
<head>
<meta charset="utf-8">
<title>RestWell Supply — Home</title>
<link rel="stylesheet" href="https://fonts.googleapis.com/css2?family=Exo+2:wght@500;600;700&family=Roboto:wght@400;500;700&display=swap">
<style>
:root{
  --blue:#2c4f9e;
  --blue-dark:#24418a;
  --topbar:#5a5a5a;
  --footer-bar:#5c5c5c;
  --text:#555a60;
  --muted:#7a7f86;
  --heading:#2c4f9e;
  --panel:#f4f5f8;
  --line:#e3e5ea;
  --white:#ffffff;
  --price-old:#9aa0a6;
  --ink:#2a2d33;
}
*{box-sizing:border-box;margin:0;padding:0}
html,body{width:1200px;height:2514px;overflow:hidden}
body{font-family:"Roboto",Arial,sans-serif;color:var(--text);background:var(--white);position:relative}
.display{font-family:"Exo 2","Roboto",sans-serif}
section,header,nav,footer{position:absolute;left:0;width:1200px}

/* top bar */
.topbar{top:0;height:37px;background:var(--topbar);color:#fff;font-size:13px}
.topbar .contact{position:absolute;left:85px;top:11px;display:flex;gap:26px}
.topbar .links{position:absolute;right:85px;top:11px;display:flex;gap:18px}
.topbar span{display:inline-flex;align-items:center;gap:6px}
.topbar svg{width:12px;height:12px;fill:#fff}

/* header */
.masthead{top:37px;height:100px;background:var(--white)}
.brand{position:absolute;left:85px;top:36px;display:flex;align-items:center;gap:10px;font-family:"Exo 2",sans-serif;font-weight:700;font-size:28px;color:var(--blue)}
.brand i{display:block;width:22px;height:22px;border-radius:50%;background:var(--blue)}
.search{position:absolute;left:516px;top:30px;display:flex;height:38px}
.search .field{width:290px;border:1px solid #cfd2d8;border-right:none;border-radius:3px 0 0 3px;font-size:12px;color:#9aa0a6;display:flex;align-items:center;gap:8px;padding-left:12px}
.search .field svg{width:12px;height:12px;stroke:#777;fill:none;stroke-width:2}
.search .btn{width:95px;background:#666a70;color:#fff;font-size:12px;font-weight:500;display:flex;align-items:center;justify-content:center;border-radius:0 3px 3px 0}
.cart{position:absolute;left:910px;top:30px;display:flex;align-items:center;gap:10px;font-size:12px;color:#666;text-transform:uppercase}
.cart b{width:40px;height:38px;background:var(--blue);border-radius:3px;display:flex;align-items:center;justify-content:center}
.cart svg{width:16px;height:16px;fill:#fff}

/* nav */
.mainnav{top:137px;height:54px;background:var(--blue)}
.mainnav ul{list-style:none;display:flex;margin-left:85px;width:1030px;height:54px}
.mainnav li{flex:1;color:#fff;font-size:13px;font-weight:500;display:flex;align-items:center;justify-content:center;border-right:1px solid rgba(255,255,255,.18);text-transform:uppercase}
.mainnav li:last-child{border-right:none}

/* hero */
.hero{top:191px;height:505px;background:radial-gradient(ellipse at 60% 50%,#ffffff 0%,#f1f2f4 60%,#e4e6ea 100%)}
.hero h1{position:absolute;left:85px;top:128px;font-size:56px;font-weight:600;color:var(--blue);letter-spacing:2px}
.hero h2{position:absolute;left:85px;top:195px;font-size:17px;font-weight:500;color:#4a4e55;letter-spacing:.5px}
.hero p{position:absolute;left:85px;top:232px;width:440px;font-size:12.5px;line-height:27px;color:var(--muted)}
.button{display:inline-flex;align-items:center;justify-content:center;background:var(--blue);color:#fff;font-size:15px;font-weight:500;border-radius:3px;text-transform:uppercase;letter-spacing:.5px}
.hero .button{position:absolute;left:85px;top:337px;width:135px;height:40px}
.hero .visual{position:absolute;left:570px;top:60px;width:510px;height:394px;border-radius:28px;background:linear-gradient(145deg,#4a4d53 0%,#1f2125 55%,#3b3e44 100%)}
.hero .dots{position:absolute;left:565px;top:470px;display:flex;gap:4px}
.hero .dots i{width:14px;height:14px;border:1.5px solid #8a8f96;border-radius:50%}
.hero .dots i.on{background:#8a8f96;box-shadow:inset 0 0 0 2px #eef0f2}

/* why */
.why{top:696px;height:414px}
.section-title{font-family:"Exo 2",sans-serif;font-weight:700;color:var(--heading);font-size:21px;letter-spacing:1px;text-transform:uppercase}
.why .section-title{position:absolute;left:87px;top:56px}
.why .copy{position:absolute;left:85px;top:100px;width:485px}
.why .copy p{font-size:12px;line-height:27px;color:var(--muted);margin-bottom:13px}
.why .button{position:absolute;left:85px;top:317px;width:148px;height:40px}
.why .video{position:absolute;left:615px;top:55px;width:500px;height:302px;background:linear-gradient(120deg,#c9ced4 0%,#8d97a3 45%,#e3e6ea 100%)}
.why .play{position:absolute;left:223px;top:129px;width:54px;height:40px;background:#e52d27;border-radius:10px;display:flex;align-items:center;justify-content:center}
.why .play svg{width:18px;height:18px;fill:#fff}

/* featured */
.featured{top:1110px;height:558px;background:var(--panel);text-align:center}
.featured .section-title{position:absolute;left:0;width:1200px;top:36px}
.subline{font-size:12.5px;color:var(--muted)}
.featured .subline{position:absolute;left:0;width:1200px;top:74px}
.tabs{position:absolute;left:0;width:1200px;top:117px;display:flex;justify-content:center;gap:22px;font-size:11.5px;font-weight:700;color:#3c4046;text-transform:uppercase}
.tabs .active{color:var(--blue);text-decoration:underline;text-underline-offset:4px}
.tabs .sep{color:#999;font-weight:400}
.cards{position:absolute;left:85px;top:164px;display:flex;gap:16px}
.card{width:247px;height:342px;background:#fff;border:1px solid var(--line)}
.card .thumb{margin:12px auto 0;width:223px;height:140px;border:1px solid var(--line);background:linear-gradient(180deg,#f7f8fa,#eceef1);position:relative}
.card .thumb span{position:absolute;left:40px;top:30px;width:143px;height:80px;border-radius:12px}
.thumb.dark span{background:linear-gradient(145deg,#50535a,#1c1e22)}
.thumb.silver span{background:linear-gradient(145deg,#a7abb1,#4d5057)}
.thumb.light span{background:linear-gradient(145deg,#dfe2e6,#9aa0a8)}
.price{margin-top:38px;font-size:18px;font-weight:700;color:var(--blue)}
.price s{color:var(--price-old);font-weight:400;margin-right:8px}
.card h3{margin-top:12px;font-size:15px;font-weight:400;color:var(--ink);text-transform:uppercase}
.actions{margin-top:14px;display:flex;justify-content:center;gap:8px}
.actions i{width:30px;height:30px;border:1px solid #cfd2d8;border-radius:50%;display:flex;align-items:center;justify-content:center}
.actions svg{width:12px;height:12px;fill:none;stroke:#777;stroke-width:2}

/* mailing */
.mailing{top:1668px;height:162px;background:var(--blue)}
.mailing .visual{position:absolute;left:84px;top:-16px;width:244px;height:192px;border-radius:24px;background:linear-gradient(145deg,#55585f 0%,#1d1f23 60%,#43464c 100%)}
.mailing .small{position:absolute;left:368px;top:40px;font-family:"Exo 2",sans-serif;font-size:27px;font-weight:500;color:#fff;letter-spacing:1px}
.mailing .big{position:absolute;left:368px;top:82px;font-family:"Exo 2",sans-serif;font-size:27px;font-weight:700;color:#fff;letter-spacing:.5px}

/* testimonials */
.testimonials{top:1830px;height:352px}
.testimonials .section-title{position:absolute;left:0;width:1200px;text-align:center;top:46px}
.testimonials .subline{position:absolute;left:0;width:1200px;text-align:center;top:85px}
.quote{position:absolute;top:138px;width:320px}
.quote .mark{position:absolute;left:0;top:-6px;font-family:Georgia,serif;font-size:30px;color:#666}
.quote p{margin-left:26px;font-size:12.5px;line-height:25px;color:var(--muted)}
.quote .close{position:absolute;right:-4px;top:92px;font-family:Georgia,serif;font-size:30px;color:#666}
.quote .who{margin:12px 0 0 26px;font-size:13.5px;font-weight:700;color:var(--blue)}
.quote .when{margin:8px 0 0 26px;font-size:12px;color:var(--muted)}

/* footer */
.site-footer{top:2182px;height:268px;background:var(--panel)}
.col{position:absolute;top:56px}
.col h4{font-size:14.5px;font-weight:700;color:#3a3e44;text-transform:uppercase;letter-spacing:.5px;margin-bottom:22px}
.col ul{list-style:none}
.col li{font-size:12px;color:var(--muted);height:25.5px;display:flex;align-items:center;gap:14px}
.col li::before{content:"";border-left:5px solid #666;border-top:4px solid transparent;border-bottom:4px solid transparent}
.cards-accepted{display:flex;gap:4px}
.cards-accepted i{width:38px;height:24px;border-radius:2px}
.social{position:absolute;left:85px;top:158px;display:flex;gap:6px}
.social i{width:33px;height:33px;border:1px solid #c8ccd2;border-radius:50%}
.contact-list li::before{display:none}
.contact-list svg{width:14px;height:14px;fill:#888;flex:none}
.bottombar{top:2450px;height:64px;background:var(--footer-bar);color:#fff;font-size:12px;text-align:center;line-height:64px}
</style>
</head>
<body>

<header class="topbar">
  <div class="contact">
    <span><svg viewBox="0 0 24 24"><path d="M6.6 10.8a15 15 0 0 0 6.6 6.6l2.2-2.2a1 1 0 0 1 1-.25 11.4 11.4 0 0 0 3.6.57 1 1 0 0 1 1 1V20a1 1 0 0 1-1 1A17 17 0 0 1 3 4a1 1 0 0 1 1-1h3.5a1 1 0 0 1 1 1c0 1.25.2 2.45.57 3.57a1 1 0 0 1-.25 1z"/></svg>Call : 0400-555-182</span>
    <span><svg viewBox="0 0 24 24"><path d="M2 5h20v14H2zm2 2v.5l8 5 8-5V7z"/></svg>Email : www.shop.restwellsupply.example</span>
  </div>
  <div class="links">
    <span><svg viewBox="0 0 24 24"><path d="M12 21 3.5 12.5A5 5 0 0 1 12 5.6a5 5 0 0 1 8.5 6.9z"/></svg>My wishlist</span>
    <span><svg viewBox="0 0 24 24"><path d="M5 3h14v18H5z"/></svg>My Quotes</span>
    <span><svg viewBox="0 0 24 24"><circle cx="12" cy="8" r="4"/><path d="M4 21a8 8 0 0 1 16 0z"/></svg>My Account</span>
    <span><svg viewBox="0 0 24 24"><path d="M4 12h12l-4-4 1.4-1.4L20 13l-6.6 6.4L12 18l4-4H4z"/></svg>Checkout</span>
    <span><svg viewBox="0 0 24 24"><path d="M4 4h16v12H8l-4 4z"/></svg>Blog</span>
  </div>
</header>

<header class="masthead">
  <div class="brand"><i></i>RestWell Supply</div>
  <div class="search">
    <div class="field"><svg viewBox="0 0 24 24"><circle cx="10" cy="10" r="7"/><path d="m15 15 6 6"/></svg>Enter Your Keyword....</div>
    <div class="btn">SEARCH</div>
  </div>
  <div class="cart"><b><svg viewBox="0 0 24 24"><path d="M2 3h3l2.5 11h11L21 6H7"/><circle cx="9" cy="19" r="2"/><circle cx="17" cy="19" r="2"/></svg></b>Shopping cart (0): items</div>
</header>

<nav class="mainnav">
  <ul><li>Home</li><li>About Us</li><li>Contact Us</li><li>Franchise</li><li>New Arrivals</li><li>Finance</li><li>Shop</li></ul>
</nav>

<section class="hero">
  <h1 class="display">RESTWELL</h1>
  <h2>MAKING SLEEP APNEA HEALTHCARE MORE AFFORDABLE</h2>
  <p>The Automatic Positive Airway Pressure (APAP) machines are set up with a minimum and maximum setting. The auto machine adjusts up and down between this the sleep period to treat Obstructive Sleep Apnea..</p>
  <span class="button">Shop Now</span>
  <div class="visual" role="img" aria-label="Product photo of a black and silver auto CPAP machine with attached humidifier"></div>
  <div class="dots"><i></i><i class="on"></i><i></i><i></i></div>
</section>

<section class="why">
  <h2 class="section-title">Why of our business</h2>
  <div class="copy">
    <p>Pronounced C-PAP, Constant Positive Airway Pressure (CPAP) machines treat Obstructive Sleep Apnea (OSA). They are set to the treatment pressure the patient's body requires (we do this for you free of charge). This treatment pressure is the pressure required to keep the patient's airway open during sleep. This is usually based on a sleep study and doctor's prescription or a previous CPAP machine setting.</p>
    <p>This treatment pressure is the pressure required to keep the patient's airway open during sleep. This is usually based on a sleep study and doctor's prescription...</p>
  </div>
  <span class="button">Watch Video</span>
  <div class="video" role="img" aria-label="Video still of a doctor consulting with an older patient at a desk">
    <div class="play"><svg viewBox="0 0 24 24"><path d="M7 4v16l13-8z"/></svg></div>
  </div>
</section>

<section class="featured">
  <h2 class="section-title">Featured Products</h2>
  <p class="subline">This treatment pressure is the pressure required to keep the patient's airway open during sleep.</p>
  <div class="tabs"><span class="active">Tops Sellers</span><span class="sep">|</span><span>Premium Range</span></div>
  <div class="cards">
    <article class="card">
      <div class="thumb dark" role="img" aria-label="Photo of a CPAP starter kit machine"><span></span></div>
      <div class="price"><s>$950.00</s>$690.00</div>
      <h3>Machine - Starter Kit</h3>
      <div class="actions"><i><svg viewBox="0 0 24 24"><path d="M2 3h3l2.5 11h11L21 6H7"/></svg></i><i><svg viewBox="0 0 24 24"><path d="M12 21 3.5 12.5A5 5 0 0 1 12 5.6a5 5 0 0 1 8.5 6.9z"/></svg></i><i><svg viewBox="0 0 24 24"><path d="M4 8h16l-4-4M20 16H4l4 4"/></svg></i></div>
    </article>
    <article class="card">
      <div class="thumb light" role="img" aria-label="Photo of a humidifier with masks and tubing"><span></span></div>
      <div class="price"><s>$1,199.00</s>$800.00</div>
      <h3>Ecosoft Humidifier</h3>
      <div class="actions"><i><svg viewBox="0 0 24 24"><path d="M2 3h3l2.5 11h11L21 6H7"/></svg></i><i><svg viewBox="0 0 24 24"><path d="M12 21 3.5 12.5A5 5 0 0 1 12 5.6a5 5 0 0 1 8.5 6.9z"/></svg></i><i><svg viewBox="0 0 24 24"><path d="M4 8h16l-4-4M20 16H4l4 4"/></svg></i></div>
    </article>
    <article class="card">
      <div class="thumb dark" role="img" aria-label="Photo of a travel auto CPAP with power adapter"><span></span></div>
      <div class="price"><s>$950.00</s>$690.00</div>
      <h3>Nightline II Auto CPAP</h3>
      <div class="actions"><i><svg viewBox="0 0 24 24"><path d="M2 3h3l2.5 11h11L21 6H7"/></svg></i><i><svg viewBox="0 0 24 24"><path d="M12 21 3.5 12.5A5 5 0 0 1 12 5.6a5 5 0 0 1 8.5 6.9z"/></svg></i><i><svg viewBox="0 0 24 24"><path d="M4 8h16l-4-4M20 16H4l4 4"/></svg></i></div>
    </article>
    <article class="card">
      <div class="thumb silver" role="img" aria-label="Photo of a silver auto CPAP machine"><span></span></div>
      <div class="price"><s>$950.00</s>$690.00</div>
      <h3>Nova GII 2.4 Auto</h3>
      <div class="actions"><i><svg viewBox="0 0 24 24"><path d="M2 3h3l2.5 11h11L21 6H7"/></svg></i><i><svg viewBox="0 0 24 24"><path d="M12 21 3.5 12.5A5 5 0 0 1 12 5.6a5 5 0 0 1 8.5 6.9z"/></svg></i><i><svg viewBox="0 0 24 24"><path d="M4 8h16l-4-4M20 16H4l4 4"/></svg></i></div>
    </article>
  </div>
</section>

<section class="mailing">
  <div class="visual" role="img" aria-label="Product photo of a black CPAP machine with humidifier"></div>
  <p class="small">STAY UP TO DATE</p>
  <p class="big">JOIN OUR MAILING LIST &amp; RECEIVE $50 DISCOUNT</p>
</section>

<section class="testimonials">
  <h2 class="section-title">Our Testimonials</h2>
  <p class="subline">This treatment pressure is the pressure required to keep the patient's airway open during sleep.</p>
  <blockquote class="quote" style="left:85px">
    <span class="mark">&ldquo;</span>
    <p>After being diagnosed with severe sleep apnea I was given the option of buying a machine for the sum plus mask. As a pensioner this was beyond my reach. important that I use a CPAP machine....</p>
    <span class="close">&rdquo;</span>
    <div class="who">Mark T. — Fernvale, NSW</div>
    <div class="when">Posed on 05 Mar 2017</div>
  </blockquote>
  <blockquote class="quote" style="left:440px">
    <span class="mark">&ldquo;</span>
    <p>After being diagnosed with severe sleep apnea I was given the option of buying a machine for the sum plus mask. As a pensioner this was beyond my reach. important that I use a CPAP machine....</p>
    <span class="close">&rdquo;</span>
    <div class="who">Rosalind</div>
    <div class="when">Posed on 05 Mar 2017</div>
  </blockquote>
  <blockquote class="quote" style="left:795px">
    <span class="mark">&ldquo;</span>
    <p>After being diagnosed with severe sleep apnea I was given the option of buying a machine for the sum plus mask. As a pensioner this was beyond my reach. important that I use a CPAP machine....</p>
    <span class="close">&rdquo;</span>
    <div class="who">Oakridge, Queensland</div>
    <div class="when">Posed on 05 Mar 2017</div>
  </blockquote>
</section>

<footer class="site-footer">
  <div class="col" style="left:93px">
    <h4>Payments Accepted</h4>
    <div class="cards-accepted"><i style="background:#3d5aa8"></i><i style="background:#d9862b"></i><i style="background:#4a7fc0"></i><i style="background:#e2793a"></i></div>
  </div>
  <div class="social"><i></i><i></i><i></i><i></i><i></i></div>
  <div class="col" style="left:340px">
    <h4>Information</h4>
    <ul><li>Promotions</li><li>About Us</li><li>Bookmark Us</li><li>Blog</li><li>Contact Us</li><li>External Links</li></ul>
  </div>
  <div class="col" style="left:523px">
    <h4>Customer Service</h4>
    <ul><li>Refunds, Warranty and Returns</li><li>Shipping and Pick Ups</li><li>Special Offers</li><li>Surveys</li><li>TGA</li><li>Videos</li></ul>
  </div>
  <div class="col" style="left:755px">
    <h4>My Account</h4>
    <ul><li>My account</li><li>Orders</li><li>Addresses</li><li>Shopping cart</li><li>Wishlist</li></ul>
  </div>
  <div class="col" style="left:922px">
    <h4>Contact Us</h4>
    <ul class="contact-list">
      <li><svg viewBox="0 0 24 24"><path d="M6.6 10.8a15 15 0 0 0 6.6 6.6l2.2-2.2a1 1 0 0 1 1-.25 11.4 11.4 0 0 0 3.6.57 1 1 0 0 1 1 1V20a1 1 0 0 1-1 1A17 17 0 0 1 3 4a1 1 0 0 1 1-1h3.5a1 1 0 0 1 1 1c0 1.25.2 2.45.57 3.57a1 1 0 0 1-.25 1z"/></svg>1300 55 0192 &nbsp;(Phone)</li>
      <li><svg viewBox="0 0 24 24"><path d="M5 9h14v11H5zM8 3h8v5H8z"/></svg>(02) 5550 1874 &nbsp;(Fax)</li>
      <li><svg viewBox="0 0 24 24"><path d="M2 5h20v14H2zm2 2v.5l8 5 8-5V7z"/></svg><u>info@restwellsupply.example</u></li>
      <li><svg viewBox="0 0 24 24"><path d="M12 2a7 7 0 0 0-7 7c0 5 7 13 7 13s7-8 7-13a7 7 0 0 0-7-7zm0 9.5A2.5 2.5 0 1 1 12 6.5a2.5 2.5 0 0 1 0 5z"/></svg>PO Box 204 | Glenmore, NSW 2790</li>
    </ul>
  </div>
</footer>

<footer class="bottombar">© Copyright 2017 RestWell Supply All Rights Reserved</footer>

</body>
</html>
```